I need a design for my company's core values statement. This will be used on large posters (one as large as a wall), small posters, mouse pads, website, etc. I only need design, not content. The content should not change.

This is an IT company so it should be modern and impressive. Clean, sleek, professional are important guidelines. Our name is The Norventa Group so space designs are not out of the question as long as they are not cliché or cheesey.

The values themselves should be the focus.

Here is the Core Values Statement as it is today:

THE NORVENTA GROUP CORE VALUES

The Norventa Group has resolved to make it clear to all stakeholders that we are a company which holds to certain core values and extolls the underlying virtues of that collective corporate conscience. Let it be known that following are the Core Values on which we base our personal behavior, our business dealings, and our daily decisions. Each member of the Norventa organization is held to these high standards on all levels of employment, interaction, and association.

THE NORVENTA GROUP’S GUIDING PRINCIPLE:

“Treat everyone with the same high level of respect and care that customers receive.”
This principle applies to everyone we come in contact within the course of doing business while working for THE NORVENTA GROUP. It pertains to clients of course, but also to colleagues, peers, subordinates, internal clients, vendors, and visitors.

OUR CORE VALUES

DELIVER EXCELLENCE
Exceed expectations.

BUILD TRUST
Through honesty, accountability, transparency, and accessibility.

BE A PEOPLE PERSON
Treat everyone with dignity and respect.

CREATE VALUE
Create and constantly deliver more value.
I
NNOVATE
Dream, innovate, create.

OWN IT
Take ownership.

Target Market(s)

International employees, clients, vendors

Industry/Entity Type

Business

Requirements
Must have
• Sleek, clean, modern, impressive. The values must be the focus
Nice to have
• We have a logo that I am attaching. it would be good to include, but not necessary.

```html
<!DOCTYPE html>
<html lang="en">
<head>
<meta charset="utf-8">
<title>The Norventa Group — Core Values</title>
<link rel="stylesheet" href="https://fonts.googleapis.com/css2?family=Montserrat:wght@200;300;400;600;700&display=swap">
<style>
  :root {
    --field: #61a852;
    --ink: #ffffff;
    --ghost: #9ccf8d;
  }
  html, body {
    margin: 0;
    padding: 0;
    overflow: hidden;
    background: var(--field);
  }
  .poster {
    position: relative;
    width: 848px;
    height: 1200px;
    overflow: hidden;
    background: var(--field);
    font-family: "Montserrat", sans-serif;
    color: var(--ink);
  }
  .tilt {
    position: absolute;
    left: var(--x);
    top: var(--y);
    transform-origin: 0 0;
    white-space: nowrap;
    line-height: 1;
    margin: 0;
  }
  .down { transform: rotate(45deg); }
  .up { transform: rotate(-45deg); }

  .value-title {
    font-weight: 300;
    text-transform: uppercase;
    letter-spacing: 0.02em;
  }
  .value-note {
    font-weight: 300;
    letter-spacing: 0.02em;
  }
  .ghost-title {
    font-weight: 200;
    color: var(--ghost);
    text-transform: uppercase;
    font-size: 94px;
    letter-spacing: 0.03em;
  }
  .statement {
    white-space: normal;
    font-size: 10px;
    line-height: 1.3;
    font-weight: 600;
    letter-spacing: 0.03em;
  }
  .statement h2 {
    font-size: 10px;
    font-weight: 700;
    text-transform: uppercase;
    margin: 0 0 6px;
    letter-spacing: 0.04em;
  }
  .statement p { margin: 0; }

  .innovate    { --x: 108px; --y: 300px; font-size: 72px; }
  .innovate-n  { --x: 86px;  --y: 366px; font-size: 19px; }
  .own-it      { --x: 212px; --y: 540px; font-size: 38px; }
  .own-it-n    { --x: 190px; --y: 575px; font-size: 16px; }
  .excellence  { --x: 50px;  --y: 940px; font-size: 71px; letter-spacing: 0.04em; }
  .excellence-n{ --x: 92px;  --y: 1002px; font-size: 19px; }
  .people      { --x: 408px; --y: 688px; font-size: 45px; }
  .people-n    { --x: 447px; --y: 722px; font-size: 17px; }
  .trust       { --x: 381px; --y: 669px; font-size: 58px; letter-spacing: 0.14em; }
  .trust-n     { --x: 367px; --y: 728px; font-size: 14.5px; letter-spacing: 0; }
  .value       { --x: 438px; --y: 843px; font-size: 44px; letter-spacing: 0.06em; }
  .value-n     { --x: 410px; --y: 879px; font-size: 15px; }

  .ghost-our    { --x: 252px; --y: 124px; }
  .ghost-core   { --x: 194px; --y: 182px; }
  .ghost-values { --x: 136px; --y: 240px; }

  .about     { --x: 268px; --y: 150px; width: 196px; }
  .principle { --x: 478px; --y: 760px; width: 372px; }
</style>
</head>
<body>
<main class="poster">
  <h1 class="tilt down ghost-title ghost-our">Our</h1>
  <div class="tilt down ghost-title ghost-core" aria-hidden="true">Core</div>
  <div class="tilt down ghost-title ghost-values" aria-hidden="true">Values</div>

  <section class="tilt up statement about">
    <h2>The Norventa Group<br>Core Values</h2>
    <p>The Norventa Group has resolved to make it clear to all stakeholders that we are a company which holds to certain core values and extolls the underlying virtues of that collective corporate conscience. Let it be known that following are the Core Values on which we base our personal behavior, our business dealings, and our daily decisions. Each member of the Norventa organization is held to these high standards on all levels of employment, interaction, and association.</p>
  </section>

  <div class="tilt down value-title innovate">Innovate</div>
  <div class="tilt down value-note innovate-n">Dream, innovate, create.</div>

  <div class="tilt down value-title own-it">Own it</div>
  <div class="tilt down value-note own-it-n">Take ownership.</div>

  <div class="tilt up value-title excellence">Deliver Excellence</div>
  <div class="tilt up value-note excellence-n">Exceed expectations.</div>

  <div class="tilt up value-title people">Be a People Person</div>
  <div class="tilt up value-note people-n">Treat everyone with dignity and respect.</div>

  <div class="tilt down value-title trust">Build Trust</div>
  <div class="tilt down value-note trust-n">Through honesty, accountability, transparency, and accessibility.</div>

  <div class="tilt down value-title value">Create Value</div>
  <div class="tilt down value-note value-n">Create and constantly deliver more value.</div>

  <section class="tilt up statement principle">
    <h2>The Norventa Group’s Guiding Principle:</h2>
    <p>“Treat everyone with the same high level of respect and care that customers receive.” This principle applies to everyone we come in contact within the course of doing business while working for the Norventa Group. It pertains to clients of course, but also to colleagues, peers, subordinates, internal clients, vendors, and visitors.</p>
  </section>
</main>
</body>
</html>
```